Design multilingual product image for email marketing

I have a product and have now introduced the following languages for it:
1. English
2. Chinese
3. Arabic
4. Spanish
5. French
6. Polish
7. Italian
8. Turkish

I have screenshot the device on the exact same page to show the different translation.

TASK: I want you to design an image/post that promotes the above languages that are now available. I was thinking maybe have my device, then multiple screen/windows popping out of it - where each one is a different language?

```html
<!DOCTYPE html>
<html lang="en">
<head>
<meta charset="utf-8">
<title>New Language Update</title>
<link rel="stylesheet" href="https://fonts.googleapis.com/css2?family=Anton&family=Noto+Sans:wght@300;400&family=Noto+Sans+SC:wght@400&family=Noto+Sans+Arabic:wght@400&display=swap">
<style>
  :root {
    --backdrop: #aebfbf;
    --navy-deep: #0f1240;
    --navy: #1c1f63;
    --indigo: #2a2c86;
    --accent-orange: #d9793a;
    --accent-blue: #3f7fd6;
    --text-light: #ffffff;
    --device-blue: #2f73c9;
    --device-dark: #16181d;
  }
  * { box-sizing: border-box; margin: 0; padding: 0; }
  html, body {
    width: 1200px; height: 960px; overflow: hidden;
    background: var(--backdrop);
  }
  .canvas {
    position: relative; width: 1200px; height: 960px;
    background: var(--backdrop);
  }
  .flyer {
    position: absolute; left: 289px; top: 40px;
    width: 622px; height: 880px; overflow: hidden;
    background: radial-gradient(ellipse at 60% 45%, var(--indigo) 0%, var(--navy) 45%, var(--navy-deep) 100%);
  }
  .flyer-lines { position: absolute; inset: 0; width: 100%; height: 100%; }
  .headline {
    position: absolute; left: 26px; top: 30px;
    font-family: "Anton", "Oswald", sans-serif;
    font-size: 84px; line-height: 86px;
    letter-spacing: 1px;
    color: var(--text-light);
    text-transform: uppercase;
  }
  .language-list {
    position: absolute; left: 56px; top: 318px;
    list-style: none;
  }
  .language-item {
    display: flex; align-items: center;
    height: 53.5px;
    font-family: "Noto Sans", "Noto Sans SC", "Noto Sans Arabic", sans-serif;
    font-weight: 300; font-size: 40px;
    color: var(--text-light);
  }
  .language-item .pointer { width: 52px; height: 30px; margin-right: 18px; flex: none; }
  .device-visual {
    position: absolute; left: 362px; top: 236px;
    width: 236px; height: 578px;
  }
</style>
</head>
<body>
<main class="canvas">
  <section class="flyer">
    <svg class="flyer-lines" viewBox="0 0 622 880" aria-hidden="true">
      <polygon points="0,0 330,0 0,330" fill="#0d1038" opacity="0.55"/>
      <polygon points="622,420 622,880 180,880" fill="#12155000" />
      <polygon points="622,520 622,880 262,880" fill="#0d1038" opacity="0.45"/>
      <line x1="210" y1="0" x2="622" y2="412" stroke="var(--accent-orange)" stroke-width="1.5" opacity="0.8"/>
      <line x1="300" y1="0" x2="622" y2="322" stroke="var(--accent-blue)" stroke-width="1.5" opacity="0.7"/>
      <line x1="0" y1="520" x2="360" y2="880" stroke="var(--accent-blue)" stroke-width="1.5" opacity="0.6"/>
      <line x1="622" y1="500" x2="250" y2="880" stroke="var(--accent-blue)" stroke-width="2" opacity="0.7"/>
      <line x1="622" y1="560" x2="310" y2="880" stroke="var(--accent-orange)" stroke-width="1.2" opacity="0.7"/>
      <line x1="140" y1="660" x2="0" y2="800" stroke="var(--accent-orange)" stroke-width="1.2" opacity="0.6"/>
    </svg>

    <h1 class="headline">New<br>Language<br>Update</h1>

    <ul class="language-list">
      <li class="language-item"><svg class="pointer" viewBox="0 0 52 30" aria-hidden="true"><path d="M4 10h26V3l18 12-18 12v-7H4z" fill="none" stroke="#fff" stroke-width="2.4" stroke-linejoin="round"/></svg>English</li>
      <li class="language-item"><svg class="pointer" viewBox="0 0 52 30" aria-hidden="true"><path d="M4 10h26V3l18 12-18 12v-7H4z" fill="none" stroke="#fff" stroke-width="2.4" stroke-linejoin="round"/></svg><span lang="zh">中文</span></li>
      <li class="language-item"><svg class="pointer" viewBox="0 0 52 30" aria-hidden="true"><path d="M4 10h26V3l18 12-18 12v-7H4z" fill="none" stroke="#fff" stroke-width="2.4" stroke-linejoin="round"/></svg><span lang="ar">عربى</span></li>
      <li class="language-item"><svg class="pointer" viewBox="0 0 52 30" aria-hidden="true"><path d="M4 10h26V3l18 12-18 12v-7H4z" fill="none" stroke="#fff" stroke-width="2.4" stroke-linejoin="round"/></svg>Española</li>
      <li class="language-item"><svg class="pointer" viewBox="0 0 52 30" aria-hidden="true"><path d="M4 10h26V3l18 12-18 12v-7H4z" fill="none" stroke="#fff" stroke-width="2.4" stroke-linejoin="round"/></svg>Française</li>
      <li class="language-item"><svg class="pointer" viewBox="0 0 52 30" aria-hidden="true"><path d="M4 10h26V3l18 12-18 12v-7H4z" fill="none" stroke="#fff" stroke-width="2.4" stroke-linejoin="round"/></svg>Polskie</li>
      <li class="language-item"><svg class="pointer" viewBox="0 0 52 30" aria-hidden="true"><path d="M4 10h26V3l18 12-18 12v-7H4z" fill="none" stroke="#fff" stroke-width="2.4" stroke-linejoin="round"/></svg>Italiana</li>
      <li class="language-item"><svg class="pointer" viewBox="0 0 52 30" aria-hidden="true"><path d="M4 10h26V3l18 12-18 12v-7H4z" fill="none" stroke="#fff" stroke-width="2.4" stroke-linejoin="round"/></svg>Türk</li>
    </ul>

    <svg class="device-visual" viewBox="0 0 236 578" role="img" aria-label="Photo of the handheld payment terminal showing its settings screen">
      <defs>
        <linearGradient id="deviceTone" x1="0" y1="0" x2="0" y2="1">
          <stop offset="0" stop-color="var(--device-blue)"/>
          <stop offset="0.2" stop-color="var(--device-dark)"/>
          <stop offset="0.55" stop-color="#d9dce2"/>
          <stop offset="0.9" stop-color="var(--device-dark)"/>
          <stop offset="1" stop-color="var(--device-blue)"/>
        </linearGradient>
      </defs>
      <rect x="0" y="0" width="236" height="578" rx="16" fill="url(#deviceTone)"/>
    </svg>
  </section>
</main>
</body>
</html>
```